New Business Card Design Project

Target Market(s)

Passing cards out

Industry/Entity Type

Asphalt contractor

Contact Information for Business Card

Ridgefold Paving

Colors
FFC000
F8CF3A
FAE287
FDF2CF
FEFAEE
F0912C
F2A743
F7CA91
FBE8D2
FDF5EE
EE7325
F08F49
F5BC92
FAE3D3
FDF4ED

Requirements
Must have
• Asphalt
Nice to have
• Would like to have 2 pictures on it of equipment

```html
<!DOCTYPE html>
<html lang="en">
<head>
<meta charset="utf-8">
<title>Ridgefold Paving – Business Cards</title>
<link rel="stylesheet" href="https://fonts.googleapis.com/css2?family=Michroma&family=Montserrat:wght@500;700&display=swap">
<style>
  :root{
    --bg:#2b2b2b;
    --asphalt-dark:#1f1f1f;
    --asphalt-mid:#2e2e2e;
    --asphalt-light:#3a3a3a;
    --orange:#f0912c;
    --orange-bright:#f2a743;
    --orange-deep:#ee7325;
    --black:#151515;
    --white:#ffffff;
    --photo-sky:#eef0f1;
    --photo-truck:#c9ccce;
    --photo-ground:#8c8a84;
  }
  *{margin:0;padding:0;box-sizing:border-box}
  html,body{width:1200px;height:1186px;overflow:hidden;background:var(--bg)}
  .canvas{position:relative;width:1200px;height:1186px}
  .card{
    position:absolute;left:170px;width:860px;height:491px;
    border-radius:26px;overflow:hidden;
    box-shadow:0 18px 40px rgba(0,0,0,.45);
  }
  /* back of card */
  .card--back{
    top:60px;
    background:
      linear-gradient(115deg,transparent 44%,rgba(255,255,255,.06) 44%,rgba(255,255,255,.06) 50%,transparent 50%),
      radial-gradient(circle at 30% 30%,var(--asphalt-light),var(--asphalt-mid) 45%,var(--asphalt-dark));
  }
  .card--back .edge{position:absolute;left:0;right:0;bottom:0;height:16px;background:var(--orange)}
  .brand{
    position:absolute;display:flex;align-items:center;gap:18px;
    font-family:"Michroma",sans-serif;text-transform:uppercase;letter-spacing:2px;
  }
  .brand__dot{width:38px;height:38px;border-radius:50%;background:var(--orange);flex:none}
  .card--back .brand{left:90px;top:200px;font-size:40px;color:var(--white)}
  /* front of card */
  .card--front{top:635px;background:var(--black)}
  .photo{
    position:absolute;inset:0;
    background:linear-gradient(180deg,var(--photo-sky) 0%,var(--photo-truck) 40%,#b3b5b6 60%,var(--photo-ground) 100%);
  }
  .card--front .brand{left:240px;top:120px;font-size:30px;color:var(--black)}
  .bands{position:absolute;inset:0}
  .name{
    position:absolute;display:flex;align-items:center;
    font-family:"Michroma",sans-serif;font-size:22px;line-height:1;white-space:nowrap;
    color:var(--white);text-transform:uppercase;letter-spacing:1px;
  }
  .name--left{left:50px;top:305px;height:55px}
  .name--right{left:530px;width:330px;top:230px;height:60px;justify-content:center}
  .contact{position:absolute;left:50px;top:385px;list-style:none;
    font-family:"Montserrat",sans-serif;font-weight:500;font-size:19px;color:var(--white)}
  .contact li{display:flex;align-items:center;gap:14px;margin-bottom:10px}
  .contact__icon{width:26px;height:26px;border-radius:5px;background:var(--orange);display:flex;align-items:center;justify-content:center}
</style>
</head>
<body>
<main class="canvas">

  <section class="card card--back" aria-label="Card back">
    <div class="brand"><span class="brand__dot"></span><span>Ridgefold Paving</span></div>
    <div class="edge"></div>
  </section>

  <section class="card card--front" aria-label="Card front">
    <div class="photo" role="img" aria-label="Photo of white tanker trucks and dump trucks parked on a gravel lot"></div>
    <div class="brand"><span class="brand__dot"></span><span>Ridgefold Paving</span></div>

    <svg class="bands" viewBox="0 0 860 491" aria-hidden="true">
      <defs>
        <linearGradient id="orangeBand" x1="0" x2="1">
          <stop offset="0" stop-color="#f2a743"/>
          <stop offset="1" stop-color="#f0912c"/>
        </linearGradient>
      </defs>
      <polygon points="470,230 860,230 860,290 520,290" fill="url(#orangeBand)"/>
      <polygon points="0,360 430,360 520,290 860,290 860,491 0,491" fill="#151515"/>
      <polygon points="0,305 450,305 405,360 0,360" fill="url(#orangeBand)"/>
      <polygon points="0,475 860,475 860,491 0,491" fill="#f0912c"/>
    </svg>

    <div class="name name--right">Dusty Morrow</div>
    <div class="name name--left">Caleb Morrow</div>

    <ul class="contact">
      <li>
        <span class="contact__icon">
          <svg width="16" height="16" viewBox="0 0 24 24"><path fill="#fff" d="M6.6 10.8a15 15 0 0 0 6.6 6.6l2.2-2.2c.3-.3.7-.4 1-.2 1.1.4 2.3.6 3.6.6.6 0 1 .4 1 1V20c0 .6-.4 1-1 1A17 17 0 0 1 3 4c0-.6.4-1 1-1h3.5c.6 0 1 .4 1 1 0 1.3.2 2.5.6 3.6.1.3 0 .7-.2 1z"/></svg>
        </span>
        <span>903 555-0148</span>
      </li>
      <li>
        <span class="contact__icon">
          <svg width="16" height="16" viewBox="0 0 24 24"><path fill="#fff" d="M3 5h18v14H3zm2 2v.5l7 4.5 7-4.5V7zm0 2.9V17h14V9.9l-7 4.5z"/></svg>
        </span>
        <span>ridgefoldpaving@mail.com</span>
      </li>
    </ul>
  </section>

</main>
</body>
</html>
```